Business Card for Makeup Artist

I need a business card designed for my makeup and hair artistry business which is primarily events and weddings focused. The card needs to be sleek, simple, stylish and appealing to women. I would prefer a white background but open to suggestions also. I also love the marble background look. I have attached some example pics. It needs to be a double sided card with logo and/or design on one side and contact details in the centre of the card on the other side. NO LOGO ON BACK. Examples attached.

Target Market(s)

Females age 14-55

Industry/Entity Type

Business

Contact Information for Business Card

Nora Vint
Principal Makeup Artist
P: 0413 925 214
E: nora@lumirabeauty.com.au
W: www.lumirabeauty.com.au

Requirements
Should not have
• No yellow, green, red or blue in the design.

```html
<!DOCTYPE html>
<html lang="en">
<head>
<meta charset="utf-8">
<title>Lumira Makeup Artistry – Business Card</title>
<link rel="stylesheet" href="https://fonts.googleapis.com/css2?family=Raleway:wght@400;500&display=swap">
<style>
  :root {
    --page-bg: #e9e8e6;
    --marble-light: #f7f7f6;
    --marble-soft: #ececeb;
    --ink-grey: #525252;
    --ink-dark: #2e2e2e;
    --accent-pink: #d663ad;
    --rule-grey: #8a8a8a;
  }
  * { box-sizing: border-box; margin: 0; padding: 0; }
  html, body {
    width: 1200px;
    height: 900px;
    overflow: hidden;
    background: var(--page-bg);
    font-family: "Raleway", sans-serif;
  }
  .canvas {
    position: relative;
    width: 1200px;
    height: 900px;
  }
  .card {
    position: absolute;
    left: 320px;
    width: 560px;
    height: 340px;
    overflow: hidden;
    box-shadow: 0 4px 14px rgba(0,0,0,0.10);
  }
  .card--front { top: 90px; }
  .card--back { top: 470px; }
  .card__marble {
    position: absolute;
    inset: 0;
    background: linear-gradient(155deg, var(--marble-light) 0%, var(--marble-soft) 100%);
  }
  .card__content {
    position: relative;
    height: 100%;
  }
  .brand__name {
    position: absolute;
    left: 36px;
    top: 36px;
    font-size: 100px;
    font-weight: 500;
    letter-spacing: 6px;
    color: var(--ink-grey);
    line-height: 1;
  }
  .brand__tagline {
    position: absolute;
    right: 30px;
    top: 168px;
    font-size: 32px;
    font-weight: 400;
    letter-spacing: 2px;
    color: var(--ink-grey);
    line-height: 1;
  }
  .contact {
    display: flex;
    flex-direction: column;
    align-items: center;
    padding-top: 100px;
    text-align: center;
  }
  .contact__name {
    font-size: 27px;
    font-weight: 400;
    letter-spacing: 0.5px;
    line-height: 34px;
    color: var(--ink-dark);
  }
  .contact__name-first { color: var(--accent-pink); }
  .contact__role {
    font-size: 16px;
    line-height: 20px;
    color: var(--accent-pink);
  }
  .contact__rule {
    width: 350px;
    height: 1px;
    margin: 24px 0 20px;
    background: var(--rule-grey);
  }
  .contact__line {
    font-size: 20px;
    line-height: 28px;
    color: var(--ink-dark);
  }
</style>
</head>
<body>
<main class="canvas">
  <section class="card card--front" aria-label="Card front">
    <div class="card__marble" role="img" aria-label="White marble texture with soft grey veins"></div>
    <div class="card__content">
      <div class="brand__name">LUMIRA</div>
      <div class="brand__tagline">MAKEUP ARTISTRY</div>
    </div>
  </section>

  <section class="card card--back" aria-label="Card back">
    <div class="card__marble" role="img" aria-label="White marble texture with soft grey veins"></div>
    <div class="card__content contact">
      <p class="contact__name"><span class="contact__name-first">NORA</span> VINT</p>
      <p class="contact__role">Principal Makeup Artist</p>
      <div class="contact__rule"></div>
      <p class="contact__line">0413 925 214</p>
      <p class="contact__line">nora@lumirabeauty.com.au</p>
      <p class="contact__line">www.lumirabeauty.com.au</p>
    </div>
  </section>
</main>
</body>
</html>
```